A Label for an ECO Friendly Spirit Company

Design a label which can be used for vodka and gin (London Dry Gin). It should be Square type Like the Shape File you see in the uploads. VORK means Local Eco friendly Authentic and Fair. We want a cool and slim label that calls for eco-friendly. We want to use it for our premium
Vodka and our London Dry Gin. Please use the logo and design it in Square Type.

40%vol, 700ml

Target Market(s)

spirits and events

Industry/Entity Type

SPIRITS

Colors
00AB8E
00BBA5
67D7C9
C6EFE9
E9F9F6
59FF00
82FF00
B8FF75
E3FFCB
F4FFEA

Requirements
Must have
• Logo from VORK, Squaee Shape

```html
<!DOCTYPE html>
<html lang="en">
<head>
<meta charset="utf-8">
<title>VORK – London Dry Gin Label</title>
<link href="https://fonts.googleapis.com/css2?family=Montserrat:wght@400;500;600&display=swap" rel="stylesheet">
<style>
  :root {
    --teal: #00AB8E;
    --lime: #8DC63F;
    --white: #FFFFFF;
    --paper: #FFFFFF;
  }
  html, body {
    margin: 0;
    padding: 0;
    width: 1200px;
    height: 2453px;
    overflow: hidden;
    background: var(--paper);
  }
  .label {
    position: absolute;
    left: 50px;
    top: 676px;
    width: 1100px;
    height: 1100px;
    display: block;
  }
  .label-type { font-family: 'Montserrat', sans-serif; }
  .volume { font-size: 30px; font-weight: 500; fill: var(--teal); }
  .story { font-size: 14px; font-weight: 500; fill: var(--lime); letter-spacing: 0.4px; }
  .brand-name { font-size: 112px; font-weight: 600; fill: var(--teal); }
  .spirit-type { font-size: 24px; font-weight: 500; fill: var(--lime); letter-spacing: 5px; }
  .strength { font-size: 38px; font-weight: 600; fill: var(--white); }
</style>
</head>
<body>
<svg class="label label-type" viewBox="-410 -410 820 820" xmlns="http://www.w3.org/2000/svg" role="img" aria-label="VORK London Dry Gin label, 700ml, 40% vol">
  <!-- body -->
  <polygon class="label-body" points="0,-410 410,0 0,410 -410,0" fill="var(--teal)"/>
  <!-- stitched inner line -->
  <polygon class="stitch-line" points="0,-364 364,0 0,364 -364,0" fill="none" stroke="var(--white)" stroke-width="2.5" stroke-dasharray="22 14"/>

  <!-- volume tab -->
  <polygon class="volume-tab" points="-66,-285 66,-285 110,-239 -110,-239" fill="var(--white)"/>
  <text class="volume" x="-4" y="-251" text-anchor="middle">700ml</text>

  <!-- story text -->
  <g class="story">
    <text x="0" y="-207" text-anchor="middle">Lorem Ipsum is simply dummy</text>
    <text x="0" y="-190" text-anchor="middle">text of the printing and typesetting-</text>
    <text x="0" y="-173" text-anchor="middle">industry. Lorem Ipsum has been the indus-</text>
    <text x="0" y="-156" text-anchor="middle">try's standard dummy text ever since the</text>
    <text x="0" y="-139" text-anchor="middle">1500s, when an unknown printer took a galley of</text>
    <text x="-133" y="-122" text-anchor="middle">type and scrambled</text>
  </g>

  <!-- brand band -->
  <polygon class="brand-band" points="-298,-102 298,-102 398,0 300,100 -300,100 -398,0" fill="var(--white)"/>
  <rect class="brand-square" x="-226" y="-62" width="118" height="118" rx="14" fill="var(--teal)"/>
  <text class="brand-name" x="-80" y="37">VORK</text>

  <!-- spirit details -->
  <text class="spirit-type" x="0" y="156" text-anchor="middle">LONDON DRY GIN</text>
  <text class="strength" x="0" y="203" text-anchor="middle">40%vol</text>
</svg>
</body>
</html>
```